Discreet simple classy for adult entertainment

I would like a matte black business card with gold writing for my business. Keeping it simple. Having my following:

Lana frost
Events. Entertainment. Promotions
0491726580

or alternatively could have what i had on my previous card below but i think i prefer the above as again - discretion.

Maybe a nice gold line thru the card or some other very simple design . Or not open to ideas/ can be doublesided if any good ideas with that.

included pics of my old bus card. not sure weather i want a photo on it or not. if i do it wont be the same pic. i kinda wanted a card that was discreet so if it was in someones wallet they wouldn't neccessarily realise it was from a stripper.

Target Market(s)

men

Industry/Entity Type

Business

Contact Information for Business Card

Lana frost
0491726580

Requirements
Nice to have
• i don't know i am really open to anything. im giving my cards to guys so something they can have in their wallet that is discreet preferably.

```html
<!DOCTYPE html>
<html lang="en">
<head>
<meta charset="utf-8">
<title>Lana Frost — Business Card</title>
<link rel="stylesheet" href="https://fonts.googleapis.com/css2?family=Mulish:wght@400;600&display=swap">
<style>
  :root {
    --backdrop: #e3e3e3;
    --paper: #f1f1ef;
    --pattern-light: #d9d9d6;
    --pattern-dark: #c4c4c1;
    --gold: #c9a227;
    --gold-deep: #a8831a;
    --ink: #1a1a1a;
  }
  * { box-sizing: border-box; margin: 0; padding: 0; }
  html, body {
    width: 1200px;
    height: 900px;
    overflow: hidden;
    background: var(--backdrop);
  }
  .canvas {
    position: relative;
    width: 1200px;
    height: 900px;
  }
  .card {
    position: absolute;
    left: 180px;
    top: 210px;
    width: 840px;
    height: 480px;
    background: var(--paper);
    box-shadow: 0 10px 28px rgba(0, 0, 0, 0.12), 0 2px 4px rgba(0, 0, 0, 0.08);
    overflow: hidden;
  }
  .pattern-field {
    position: absolute;
    left: 0;
    width: 100%;
    background: linear-gradient(135deg, var(--pattern-light), var(--pattern-dark) 50%, var(--pattern-light));
  }
  .pattern-field--top { top: 0; height: 140px; }
  .pattern-field--bottom { top: 290px; height: 190px; }
  .name-band {
    position: absolute;
    left: 0;
    top: 140px;
    width: 100%;
    height: 150px;
    background: var(--paper);
    display: flex;
    flex-direction: column;
    align-items: center;
    justify-content: center;
    color: var(--ink);
    font-family: "Mulish", sans-serif;
    text-align: center;
  }
  .gold-rule {
    position: absolute;
    left: 0;
    width: 100%;
    height: 3px;
    background: linear-gradient(90deg, var(--gold-deep), var(--gold) 30%, #e0c25a 55%, var(--gold) 80%, var(--gold-deep));
  }
  .gold-rule--top { top: 140px; }
  .gold-rule--bottom { top: 287px; }
  .name {
    font-weight: 600;
    font-size: 38px;
    letter-spacing: 2px;
    text-transform: uppercase;
    line-height: 1.1;
  }
  .tagline {
    font-weight: 400;
    font-size: 20px;
    letter-spacing: 0.5px;
    margin-top: 2px;
  }
  .phone {
    font-weight: 400;
    font-size: 30px;
    letter-spacing: 1px;
    margin-top: 4px;
  }
</style>
</head>
<body>
  <main class="canvas">
    <section class="card">
      <div class="pattern-field pattern-field--top" role="img" aria-label="Repeating pattern of small black diamonds on light paper"></div>
      <div class="name-band">
        <h1 class="name">Lana Frost</h1>
        <p class="tagline">Events. Entertainment. Promotions</p>
        <p class="phone">0491726580</p>
      </div>
      <div class="pattern-field pattern-field--bottom" role="img" aria-label="Repeating pattern of small black diamonds on light paper"></div>
      <div class="gold-rule gold-rule--top"></div>
      <div class="gold-rule gold-rule--bottom"></div>
    </section>
  </main>
</body>
</html>
```